Renata Quisby

Luxury And Style -

Black - White & Gold

Target Market(s)

Fashion

Industry/Entity Type

Fashion

Requirements
Must have
• High-End
Nice to have
• We will Print on Silk Paper

```html
<!DOCTYPE html>
<html lang="en">
<head>
<meta charset="utf-8">
<title>Renata Quisby — Letterhead</title>
<link href="https://fonts.googleapis.com/css2?family=Open+Sans:wght@300;400;600;700&family=Raleway:wght@700&display=swap" rel="stylesheet">
<style>
  :root {
    --backdrop: #e2e2e2;
    --paper: #ffffff;
    --ink-black: #000000;
    --gold: #c2a165;
    --gold-dark: #b88f5c;
    --gold-light: #e3c697;
    --heading: #3f3f3f;
    --body: #8a8a8a;
    --rule-dark: #2b2b2b;
  }
  * { box-sizing: border-box; margin: 0; padding: 0; }
  html, body { width: 1200px; height: 1200px; overflow: hidden; }
  body { background: var(--backdrop); font-family: "Open Sans", sans-serif; position: relative; }

  .letterhead {
    position: absolute; left: 214px; top: 64px;
    width: 791px; height: 1103px;
    background: var(--paper);
  }
  .letterhead__header {
    position: absolute; left: 2px; top: 0; right: 0; height: 217px;
    background: var(--ink-black);
  }
  .letterhead__gold-rule {
    position: absolute; left: 2px; right: 0; top: 222px; height: 5px;
    background: var(--gold);
  }

  .brand {
    position: absolute; left: 52px; top: 110px; width: 225px;
    text-align: center; color: var(--gold);
  }
  .brand__name {
    font-weight: 400; font-size: 20px; letter-spacing: 4px;
    text-transform: uppercase; white-space: nowrap;
  }
  .brand__tagline {
    margin-top: 6px; font-weight: 300; font-size: 12.5px; letter-spacing: 0.3px;
    text-transform: uppercase;
  }

  .contact-strip {
    position: absolute; left: 538px; top: 55px; width: 25px; height: 115px;
    background: linear-gradient(180deg, var(--gold-dark), var(--gold-light) 50%, var(--gold-dark));
  }
  .contact-strip__icon { position: absolute; left: 4px; width: 17px; height: 17px; }
  .contact-strip__divider { position: absolute; left: 0; right: 0; height: 1px; background: rgba(255,255,255,0.35); }
  .contact-list {
    position: absolute; left: 571px; top: 57px;
    color: #fff; font-size: 12px; line-height: 17.5px;
  }
  .contact-list__group { margin-bottom: 3.5px; }

  .recipient { position: absolute; left: 103px; top: 272px; }
  .recipient__name { font-weight: 600; font-size: 16.5px; color: var(--heading); margin-bottom: 6px; }
  .recipient__line { font-size: 11.5px; line-height: 16px; color: var(--body); }

  .letter-body {
    position: absolute; left: 103px; top: 398px; width: 579px;
    font-size: 11.2px; line-height: 16px; color: var(--body);
    text-align: justify;
  }
  .letter-body p + p { margin-top: 16px; }

  .sign-off { position: absolute; left: 103px; top: 808px; }
  .sign-off__signature {
    width: 140px; height: 28px; border-radius: 3px;
    background: linear-gradient(90deg, #e6e6e6, #f4f4f4);
  }
  .sign-off__name {
    margin-top: 6px; font-family: "Raleway", sans-serif; font-weight: 700;
    font-size: 15px; color: var(--heading); letter-spacing: 0.2px;
  }
  .sign-off__title { margin-top: 2px; font-size: 11.5px; color: var(--body); }

  .letterhead__footer-rule {
    position: absolute; left: 0; right: 0; top: 1052px; height: 3px;
    background: var(--rule-dark);
  }
  .letterhead__footer-band {
    position: absolute; left: 0; right: 0; top: 1058px; height: 45px;
    background: linear-gradient(90deg, var(--gold-dark), var(--gold-light));
  }
</style>
</head>
<body>
  <main class="letterhead">
    <header class="letterhead__header">
      <div class="brand">
        <div class="brand__name">Renata Quisby</div>
        <div class="brand__tagline">Luxury and Style</div>
      </div>

      <div class="contact-strip" aria-hidden="true">
        <svg class="contact-strip__icon" style="top:10px" viewBox="0 0 24 24" fill="none" stroke="#fff" stroke-width="2" stroke-linecap="round" stroke-linejoin="round">
          <path d="M22 16.9v3a2 2 0 0 1-2.2 2 19.8 19.8 0 0 1-8.6-3.1 19.5 19.5 0 0 1-6-6A19.8 19.8 0 0 1 2.1 4.2 2 2 0 0 1 4.1 2h3a2 2 0 0 1 2 1.7c.1.9.4 1.9.7 2.8a2 2 0 0 1-.5 2.1L8 9.9a16 16 0 0 0 6 6l1.3-1.3a2 2 0 0 1 2.1-.4c.9.3 1.8.6 2.8.7a2 2 0 0 1 1.8 2z"/>
          <path d="M15 5a5 5 0 0 1 4 4M15 1a9 9 0 0 1 8 8"/>
        </svg>
        <div class="contact-strip__divider" style="top:38px"></div>
        <svg class="contact-strip__icon" style="top:48px" viewBox="0 0 24 24" fill="#fff">
          <path d="M12 2a7 7 0 0 0-7 7c0 5.2 7 13 7 13s7-7.8 7-13a7 7 0 0 0-7-7zm0 9.5A2.5 2.5 0 1 1 12 6.5a2.5 2.5 0 0 1 0 5z"/>
        </svg>
        <div class="contact-strip__divider" style="top:77px"></div>
        <svg class="contact-strip__icon" style="top:88px" viewBox="0 0 24 24" fill="none" stroke="#fff" stroke-width="1.8">
          <circle cx="12" cy="12" r="9.5"/>
          <path d="M2.5 12h19M12 2.5c3 3 3 16 0 19M12 2.5c-3 3-3 16 0 19"/>
        </svg>
      </div>

      <div class="contact-list">
        <div class="contact-list__group">+1 416 555 0182<br>+1 416 555 0247</div>
        <div class="contact-list__group">harbour lane Toronto<br>on Canada M4 K2R8</div>
        <div class="contact-list__group">quisbystyle.com<br>hello@quisbystyle.com</div>
      </div>
    </header>
    <div class="letterhead__gold-rule"></div>

    <section class="recipient">
      <h1 class="recipient__name">Name Surname</h1>
      <p class="recipient__line">Senior Executive</p>
      <p class="recipient__line">Address goes here. Street, City, Country</p>
      <p class="recipient__line">office@quisbystyle.com</p>
      <p class="recipient__line">416-555-0319</p>
    </section>

    <section class="letter-body">
      <p>Lorem ipsum dolor sit amet, consectetur adipisicing elit, sed do eiusmod tempor incididunt ut labore et dolore magna aliqua. Ut enim ad minim veniam, quis nostrud exercitation ullamco laboris nisi ut aliquip ex ea commodo consequat. Duis aute irure dolor in reprehenderit in voluptate velit esse cillum dolore eu fugiat nulla pariatur. Excepteur sint occaecat cupidatat non proident, sunt in culpa qui officia deserunt mollit anim id est laborum. Sed ut perspiciatis unde omnis iste natus error sit voluptatem accusantium doloremque laudantium, totam rem aperiam, eaque ipsa quae ab illo inventore veritatis et quasi architecto beatae vitae dicta sunt explicabo. Nemo enim ipsam voluptatem quia voluptas sit aspernatur aut odit aut fugit, sed quia consequuntur magni dolores eos qui ratione voluptatem sequi nesciunt. Neque porro voluptatem sequi nesciunt. Nemo enim ipsam voluptatem quia voluptas.</p>
      <p>Lorem ipsum dolor sit amet, consectetur adipisicing elit, sed do eiusmod tempor incididunt ut labore et dolore magna aliqua. Ut enim ad minim veniam, quis nostrud exercitation ullamco laboris nisi ut aliquip ex ea commodo consequat. Duis aute irure dolor in reprehenderit in voluptate velit esse cillum dolore eu fugiat nulla pariatur. Excepteur sint occaecat cupidatat non proident, sunt in culpa qui officia deserunt mollit anim id est laborum. Sed ut perspiciatis unde omnis iste natus error sit voluptatem accusantium doloremque laudantium, totam rem aperiam, eaque ipsa quae ab illo inventore veritatis et quasi architecto beatae vitae dicta sunt explicabo. Nemo enim ipsam voluptatem quia voluptas sit aspernatur aut odit aut.</p>
      <p>Lorem ipsum dolor sit amet, consectetur adipisicing elit, sed do eiusmod tempor incididunt ut labore et dolore magna aliqua. Ut enim ad minim veniam, quis nostrud exercitation ullamco laboris nisi ut aliquip ex ea commodo consequat. .</p>
    </section>

    <section class="sign-off">
      <div class="sign-off__signature" role="img" aria-label="Handwritten signature"></div>
      <div class="sign-off__name">NAME SURNAME</div>
      <div class="sign-off__title">General Manager</div>
    </section>

    <div class="letterhead__footer-rule"></div>
    <footer class="letterhead__footer-band"></footer>
  </main>
</body>
</html>
```